Business Card Design

After a corporate career in the finance sector I am now operating on my own as a consultant. I require a simple design, and want a strong card which is targeted at a conservative audience.

Target Market(s)

highly educated senior management, directors of companies, finance sector

Industry/Entity Type

Conservative

Contact Information for Business Card

Ruth Danver
Consultant
Mobile: 0417 862 450
Email: ruth.danv@mailcove.net

Requirements
Should not have
• I don't want the colours green/yellow/brown

```html
<!DOCTYPE html>
<html lang="en">
<head>
<meta charset="utf-8">
<title>Ruth Danver – Business Card</title>
<link href="https://fonts.googleapis.com/css2?family=Questrial&display=swap" rel="stylesheet">
<style>
  :root {
    --page-bg: #e6e6e4;
    --card-white: #f7f8f9;
    --ink: #1b1c1e;
    --band-black: #111214;
    --band-graphite: #55575a;
    --stripe-mid: #9b9d9f;
    --stripe-light: #d6d8da;
    --contact-text: #f2f2f2;
  }
  * { margin: 0; padding: 0; box-sizing: border-box; }
  html, body {
    width: 1200px;
    height: 1000px;
    overflow: hidden;
    background: var(--page-bg);
    font-family: "Questrial", "Century Gothic", sans-serif;
  }
  .business-card {
    position: absolute;
    left: 180px;
    top: 260px;
    width: 840px;
    height: 480px;
    border-radius: 26px;
    overflow: hidden;
    background: var(--card-white);
    box-shadow: 0 18px 40px rgba(0,0,0,0.22);
  }
  .card-wave {
    position: absolute;
    inset: 0;
    width: 840px;
    height: 480px;
  }
  .identity {
    position: absolute;
    left: 78px;
    top: 268px;
    color: var(--ink);
  }
  .identity__name {
    font-size: 52px;
    font-weight: 400;
    letter-spacing: 1px;
    line-height: 1;
  }
  .identity__role {
    margin-top: 8px;
    font-size: 26px;
    letter-spacing: 1px;
    line-height: 1;
  }
  .contact-list {
    position: absolute;
    right: 44px;
    top: 96px;
    list-style: none;
    color: var(--contact-text);
    text-align: right;
  }
  .contact-list__item {
    display: flex;
    align-items: center;
    justify-content: flex-end;
    gap: 18px;
    height: 50px;
    margin-bottom: 14px;
    white-space: nowrap;
  }
  .contact-list__phone { font-size: 30px; letter-spacing: 1.5px; }
  .contact-list__email { font-size: 23px; letter-spacing: 0.5px; }
  .contact-icon { width: 38px; height: 38px; flex: none; }
</style>
</head>
<body>
  <div class="business-card">
    <svg class="card-wave" viewBox="0 0 840 480" aria-hidden="true">
      <defs>
        <linearGradient id="bandShade" x1="0" y1="1" x2="0.6" y2="0">
          <stop offset="0" stop-color="var(--band-graphite)"/>
          <stop offset="0.35" stop-color="var(--band-black)"/>
          <stop offset="1" stop-color="var(--band-black)"/>
        </linearGradient>
      </defs>
      <path class="stripe-light" d="M400 0 C320 190 520 300 430 480 L840 480 L840 0 Z" fill="var(--stripe-light)"/>
      <path class="stripe-mid" d="M430 0 C350 190 550 300 460 480 L840 480 L840 0 Z" fill="var(--stripe-mid)"/>
      <path class="band-dark" d="M454 0 C374 190 574 300 484 480 L840 480 L840 0 Z" fill="url(#bandShade)"/>
    </svg>

    <div class="identity">
      <h1 class="identity__name">Ruth Danver</h1>
      <p class="identity__role">Consultant</p>
    </div>

    <ul class="contact-list">
      <li class="contact-list__item">
        <span class="contact-list__phone">0417 862 450</span>
        <svg class="contact-icon" viewBox="0 0 38 38" aria-label="Mobile">
          <circle cx="19" cy="19" r="17" fill="none" stroke="#f2f2f2" stroke-width="2"/>
          <rect x="14" y="11" width="10" height="16" rx="1.5" fill="none" stroke="#f2f2f2" stroke-width="1.8"/>
          <line x1="17.5" y1="24" x2="20.5" y2="24" stroke="#f2f2f2" stroke-width="1.4"/>
        </svg>
      </li>
      <li class="contact-list__item">
        <span class="contact-list__email">ruth.danv@mailcove.net</span>
        <svg class="contact-icon" viewBox="0 0 38 38" aria-label="Email">
          <circle cx="19" cy="19" r="17" fill="none" stroke="#f2f2f2" stroke-width="2"/>
          <rect x="11" y="13" width="16" height="12" fill="#f2f2f2"/>
          <polyline points="11,13 19,20 27,13" fill="none" stroke="#111214" stroke-width="1.5"/>
        </svg>
      </li>
    </ul>
  </div>
</body>
</html>
```